Fryloopmarket.com website
Turning Grease Into Fuel
Fryloopmarket.com website - Environment
Creative Brief
Environment
www.fryloopmarket.com
We are a small and scrappy collection of entrepreneurs who desire to do financially well while doing social good in the world. We are evangelists for sustainable issues. We recycle used cooking oil from restaurants and other establishments that fry food. We collect this waste oil and filter it to create recycled vegetable oil. This recycled vegetable oil is used as a feed stock to produce biodiesel which is, in turn, used in diesel cars, trucks and diesel motor of all kinds.
Like clean. modern looking sites. I like sites that integrate media: Youtube, Facebook, etc. I like my logo which I will upload for your review.
above header
I am pretty open to the design but I am in need to make a decision quickly. My last project was started and completed in less than 5 days. I would love to do the same here.
pixelmaven pixelmaven
somoxu somoxu
tarvlin tarvlin
I like draft #8 the best but I would like to incorporate the icons of draft #7 in the navigation just like the symbol is incporated into the About OilTrove tab. I also want to add the site map from draft #7 to the bottom of draft #8. The background may need to be changed to grey to accomodate this change. I would like to change the middle section on the bottom from "Our Services" to "Client Showcase" similar to draft #9
I like both #1 and #2. I like the textured background of Draft #1 and the imagery but I would like to see that images reflect the business a bit more. Draft #2 fits my layout vision and corporate motif. I like the image on the page. The green chosen for the layout works but I would like to try a slightly darker green. I worry about the site looking too "pea green" but I also don't want it to be too dark. For each Draft, I would like to see what a representation of the slides on the home page would look like. I envision that the home page would have four "slides" that rotate for each of the above referenced topics. Slide 1 would feature the OilTrove logo and a few words on the company. Slide 2 would have a graphic for "Used Cooking Oil" something like a fryer or grease barrel; Slide 3 would have a graphic for "Recycled Vegetable Oil" something like the bottle in Draft #2; and Slide 4 would have a graphic for "Biodiesel" something like a diesel gas pump or truck. These four segments are essentially the four areas for the education segment as well. In addition, I would like to see two other pages: Client Showcase and About Us. I would like to see what a Client Showcase page and About Us page would look like. The Client Showcase page will need to have the ability to integrate picture or video along with some pull out quotes for client testimonial of our service. The idea of this page is to both promote our clients, typically restaurants, by touting a special dish or recipe to the public and to highlight why recycling grease is important to them. The About Us page needs to provide an area for pictures and/or video. This page will provide a description of the company, provide a listing of press and media clippings as well as contact information for the public. It will be important that a potential client or partner that visits the About Us section take from the page a sense of what this company is all about.
Harbortilesites Harbortilesites
SiteAdmin SiteAdmin
Additional Information by Project Holder: "The site that is close to the ideal of what I am looking to achieve is listed below: http://www.brightfieldkinetichomesteads.example/ I like the graphics and how they integrate education of solar power with an explanation of their product. I would like our site to do the same for used cooking oil and biodiesel. I also have a fledgling Facebook page up for OilTrove that has three educational YouTube films posted. I also like the font they used. The integrted flash (I think) is great too."

```html
<!DOCTYPE html>
<html lang="en">
<head>
<meta charset="utf-8">
<title>OilTrove — Turning Grease Into Fuel</title>
<link rel="stylesheet" href="https://fonts.googleapis.com/css2?family=Arimo:wght@400;700&display=swap">
<style>
  :root {
    --sky-top: #9fd3ef;
    --sky-bottom: #d9eff2;
    --meadow: #b5d97a;
    --grass: #7fbf2a;
    --grass-deep: #4f8f18;
    --footer: #3f7a12;
    --footer-deep: #2f5f0c;
    --orange: #f39a1c;
    --orange-deep: #e0780c;
    --nav-green: #5aa51e;
    --nav-green-deep: #3f8512;
    --card-top: #c9e67a;
    --card-bottom: #7dbb2a;
    --white: #ffffff;
  }
  * { box-sizing: border-box; margin: 0; padding: 0; }
  html, body { width: 1200px; height: 838px; overflow: hidden; }
  body {
    position: relative;
    font-family: "Arimo", Arial, sans-serif;
    background: var(--grass);
  }
  .header-backdrop {
    position: absolute; left: 0; top: 0; width: 1200px; height: 372px;
    background: linear-gradient(to bottom, var(--sky-top) 0%, var(--sky-bottom) 60%, var(--meadow) 100%);
  }
  .grass {
    position: absolute; left: 0; top: 372px; width: 1200px; height: 348px;
    background: linear-gradient(to bottom, var(--grass) 0%, #8cc83a 30%, var(--grass-deep) 100%);
  }
  .brand { position: absolute; left: 84px; top: 14px; display: flex; align-items: center; gap: 14px; }
  .brand-mark { width: 84px; height: 84px; border-radius: 50%; background: var(--nav-green); }
  .brand-name { font-size: 44px; font-weight: 700; color: var(--orange); line-height: 1; }
  .brand-tagline { font-size: 17px; font-weight: 700; color: var(--orange); margin-top: 6px; }

  .main-nav {
    position: absolute; left: 612px; top: 29px; width: 516px; height: 38px;
    background: linear-gradient(to bottom, #7cc23a, var(--nav-green-deep));
    border-radius: 6px 6px 10px 10px;
    display: flex; align-items: center; justify-content: space-around;
    padding: 0 10px;
  }
  .main-nav a { color: var(--white); text-decoration: none; font-size: 13px; }

  .hero {
    position: absolute; left: 187px; top: 113px; width: 857px; height: 247px;
    border: 4px solid var(--orange);
    border-radius: 4px;
    background: rgba(255,255,255,0.45);
  }
  .hero-title {
    position: absolute; left: 38px; top: 42px;
    font-size: 33px; font-weight: 700; color: var(--orange); line-height: 1.15;
  }
  .hero-title span { display: block; padding-left: 118px; }
  .hero-text {
    position: absolute; left: 130px; top: 124px;
    font-size: 15px; font-weight: 700; color: var(--orange-deep); line-height: 46px;
  }
  .hero-mark {
    position: absolute; left: 907px; top: 96px; width: 148px; height: 148px;
    border-radius: 50%; background: var(--orange);
    display: flex; align-items: center; justify-content: center;
    color: var(--white); font-size: 24px; font-weight: 700;
  }

  .panels { position: absolute; top: 451px; left: 84px; width: 1034px; height: 245px; }
  .panel {
    position: absolute; top: 0; width: 240px; height: 245px;
    background: linear-gradient(to bottom, var(--card-top), var(--card-bottom));
    border-radius: 4px;
    box-shadow: 0 2px 6px rgba(0,0,0,0.2);
  }
  .panel:nth-child(1) { left: 0; }
  .panel:nth-child(2) { left: 269px; }
  .panel:nth-child(3) { left: 533px; }
  .panel:nth-child(4) { left: 794px; }
  .panel-title {
    height: 48px; line-height: 48px; text-align: center;
    background: linear-gradient(to bottom, #f9b640, var(--orange-deep));
    border-radius: 4px 4px 0 0;
    color: var(--white); font-size: 21px; font-weight: 700;
  }
  .panel-list { list-style: none; padding: 14px 0 0 20px; }
  .panel-list li {
    position: relative; padding-left: 24px; height: 37px; line-height: 37px;
    color: var(--white); font-size: 12px;
    border-bottom: 1px solid rgba(255,255,255,0.25);
    margin-right: 16px;
  }
  .panel-list li:last-child { border-bottom: none; }
  .panel-list li::before {
    content: ""; position: absolute; left: 2px; top: 14px;
    width: 9px; height: 9px; border-radius: 50%;
    background: var(--white); border: 2px solid var(--nav-green);
  }

  .site-footer {
    position: absolute; left: 0; top: 720px; width: 1200px; height: 118px;
    background: linear-gradient(to bottom, var(--footer), var(--footer-deep));
    color: var(--white);
  }
  .footer-links { position: absolute; left: 84px; top: 36px; font-size: 12px; }
  .copyright { position: absolute; left: 84px; top: 56px; font-size: 12px; font-weight: 700; }
  .legal-links { position: absolute; left: 864px; top: 30px; font-size: 13px; }
  .social { position: absolute; left: 1010px; top: 54px; display: flex; gap: 14px; }
  .social span { width: 28px; height: 28px; border-radius: 4px; }
  .social .s1 { background: #3b5a9a; }
  .social .s2 { background: #49b6e8; }
  .social .s3 { background: #e2701e; }
</style>
</head>
<body>
  <div class="header-backdrop" role="img" aria-label="Landscape of blue sky over green hills with small trees"></div>
  <div class="grass" role="img" aria-label="Green grass field"></div>

  <header class="brand">
    <div class="brand-mark"></div>
    <div>
      <div class="brand-name">OilTrove</div>
      <div class="brand-tagline">Turning Grease Into Fuel</div>
    </div>
  </header>

  <nav class="main-nav">
    <a href="#">HOME</a>
    <a href="#">ABOUTUS</a>
    <a href="#">OURSERVICES</a>
    <a href="#">CELIENTSHOWCASE</a>
    <a href="#">EDUCATIONAL</a>
  </nav>

  <section class="hero">
    <h1 class="hero-title">Turning Grease<span>Into Fuel</span></h1>
    <p class="hero-text">Phasellus ante ipsum, ornare sed<br>Tellusan posuere faucibus</p>
  </section>
  <div class="hero-mark">OilTrove</div>

  <div class="panels">
    <section class="panel">
      <h2 class="panel-title">Our Services</h2>
      <ul class="panel-list">
        <li>Raises Awareness</li><li>Influences Buying Decisions</li><li>Increases Consumer Loyalty</li><li>Drives up Product Sales</li><li>Is Affordable and Convenient</li>
      </ul>
    </section>
    <section class="panel">
      <h2 class="panel-title">Latest Updates</h2>
      <ul class="panel-list">
        <li>Raises Awareness</li><li>Influences Buying Decisions</li><li>Increases Consumer Loyalty</li><li>Drives up Product Sales</li><li>Is Affordable and Convenient</li>
      </ul>
    </section>
    <section class="panel">
      <h2 class="panel-title">Quick Links</h2>
      <ul class="panel-list">
        <li>Raises Awareness</li><li>Influences Buying Decisions</li><li>Increases Consumer Loyalty</li><li>Drives up Product Sales</li><li>Is Affordable and Convenient</li>
      </ul>
    </section>
    <section class="panel">
      <h2 class="panel-title">Fuel Advantages</h2>
      <ul class="panel-list">
        <li>Raises Awareness</li><li>Influences Buying Decisions</li><li>Increases Consumer Loyalty</li><li>Drives up Product Sales</li><li>Is Affordable and Convenient</li>
      </ul>
    </section>
  </div>

  <footer class="site-footer">
    <div class="footer-links">Home | Home | Ourservices | Celientshowcase | Educational</div>
    <div class="copyright">Copyright © 2011, OilTrove, LLC. All Rights Reserved</div>
    <div class="legal-links">Privacy Policy &nbsp;&nbsp;|&nbsp;&nbsp; Terms of Use &nbsp;&nbsp;|&nbsp;&nbsp; Site Map</div>
    <div class="social"><span class="s1"></span><span class="s2"></span><span class="s3"></span></div>
  </footer>
</body>
</html>
```